Professional, modern and unique business card. We are looking to present a new look to our business cards however we don't want to divert too far away from original template. We want social media links and our 3 office addresses on the backside of the business cards. Please see attached business card templates for ideas.
Lakeshore Realty Color Code:
R: 7
G:63
B:86

Target Market(s)

Real Estate

Industry/Entity Type

Real Estate

Contact Information for Business Card

Follow the attached templates. In need of a more modern and unique touch but don't want to divert from the original theme or color.
Lakeshore Realty Color Code:
R: 7
G:63
B:86

Font styles to use
Serif

Requirements
Must have
• Lakeshore Realty logo, Lakeshore realty colors, social media links, 3 office addresses,
Nice to have
• information about Lakeshore Realty and QR codes. You can check out www.mylakeshorehomes.example

```html
<!DOCTYPE html>
<html lang="en">
<head>
<meta charset="utf-8">
<title>Lakeshore Realty Business Card</title>
<link rel="stylesheet" href="https://fonts.googleapis.com/css2?family=Cinzel:wght@700&family=Oswald:wght@500&family=PT+Sans:wght@400&family=Crimson+Text:ital@1&display=swap">
<style>
  :root {
    --brand: #073f56;
    --brand-light: #0f5877;
    --brand-soft: #2a6f8c;
    --card-dark: #111214;
    --card-mid: #2a2c30;
    --text-light: #ffffff;
    --logo-light: #dbe8ee;
    --muted: #c9d3d8;
    --page: #e9e5df;
  }
  * { box-sizing: border-box; margin: 0; padding: 0; }
  html, body { width: 1200px; height: 800px; overflow: hidden; }
  body {
    background: var(--page);
    font-family: "PT Sans", sans-serif;
    position: relative;
  }
  .card {
    position: absolute;
    left: 300px;
    width: 600px;
    height: 330px;
    border-radius: 14px;
    overflow: hidden;
    background: radial-gradient(ellipse at 60% 45%, var(--card-mid) 0%, var(--card-dark) 65%);
    box-shadow: 0 6px 18px rgba(0,0,0,0.25);
  }
  .card-front { top: 40px; }
  .card-back { top: 420px; }
  .contact-band {
    position: absolute;
    left: 0; right: 0; bottom: 0;
    height: 82px;
    background: linear-gradient(180deg, var(--brand-light), var(--brand));
    border-top: 2px solid #3f7f99;
    color: var(--text-light);
    font-size: 15px;
  }
  .logo {
    position: absolute;
    font-family: "Cinzel", serif;
    font-weight: 700;
    text-transform: uppercase;
    line-height: 1.05;
  }
  /* Front */
  .logo-small {
    left: 34px; top: 52px;
    font-size: 28px;
    color: var(--brand-light);
  }
  .agent-name {
    position: absolute;
    left: 36px; top: 172px;
    font-family: "Oswald", sans-serif;
    font-size: 26px;
    line-height: 1.2;
    color: var(--text-light);
    letter-spacing: 0.5px;
  }
  .agent-title {
    position: absolute;
    left: 38px; top: 206px;
    font-family: "Crimson Text", serif;
    font-style: italic;
    font-size: 16px;
    line-height: 1.2;
    color: var(--brand-soft);
  }
  .agent-photo {
    position: absolute;
    left: 420px; top: 22px;
    width: 170px; height: 226px;
    background: linear-gradient(180deg, #3a3633 0%, #1c1c1e 100%);
  }
  .contact-list { position: absolute; list-style: none; }
  .contact-list li { display: flex; align-items: center; gap: 8px; height: 25px; }
  .contact-left { left: 34px; top: 18px; }
  .contact-right { right: 30px; top: 18px; text-align: right; }
  .contact-right li { justify-content: flex-end; }
  .contact-list svg { width: 14px; height: 14px; fill: var(--text-light); flex: none; }
  /* Back */
  .logo-large {
    left: 44px; top: 88px;
    font-size: 40px;
    color: var(--logo-light);
    letter-spacing: 1px;
  }
  .social-list {
    position: absolute;
    right: 40px; top: 70px;
    list-style: none;
    color: var(--text-light);
    font-size: 15px;
  }
  .social-list li {
    display: flex; align-items: center; justify-content: flex-end;
    gap: 8px; height: 25px;
  }
  .social-square {
    width: 18px; height: 18px;
    background: var(--brand-light);
    border-radius: 2px;
    flex: none;
  }
  .office-band { display: flex; align-items: center; padding: 0 26px; }
  .office {
    flex: 1;
    font-size: 14px;
    line-height: 1.2;
    padding: 0 10px;
  }
  .office + .office { border-left: 1px solid var(--muted); }
</style>
</head>
<body>

  <section class="card card-front" aria-label="Business card front">
    <div class="logo logo-small">Lakeshore<br>Realty</div>
    <div class="agent-name">EVAN CHEN</div>
    <div class="agent-title">Associate Broker</div>
    <div class="agent-photo" role="img" aria-label="Portrait photo of the agent in a dark suit"></div>
    <div class="contact-band">
      <ul class="contact-list contact-left">
        <li><svg viewBox="0 0 14 14"><rect x="4" y="1" width="6" height="12" rx="1"/></svg>555-014-2909</li>
        <li><svg viewBox="0 0 14 14"><path d="M1 5 Q7 1 13 5 L11 7 L9 5 L5 5 L3 7 Z M3 8 H11 V12 H3 Z"/></svg>555-019-2922</li>
      </ul>
      <ul class="contact-list contact-right">
        <li>555-019-2944<svg viewBox="0 0 14 14"><rect x="2" y="5" width="10" height="7" rx="1"/><rect x="4" y="1" width="6" height="4"/></svg></li>
        <li>ChenEvan@mailbox.example<svg viewBox="0 0 14 14"><path d="M1 3 H13 V11 H1 Z M1 3 L7 8 L13 3" stroke="#073f56" stroke-width="1"/></svg></li>
      </ul>
    </div>
  </section>

  <section class="card card-back" aria-label="Business card back">
    <div class="logo logo-large">Lakeshore<br>Realty</div>
    <ul class="social-list">
      <li>LakeshorerealtyNY<span class="social-square"></span></li>
      <li>Info at Lakeshore Realty<span class="social-square"></span></li>
      <li>@LakeshoreRealtyNY<span class="social-square"></span></li>
      <li>Lakeshore Realty<span class="social-square"></span></li>
      <li>Lakeshore Realty New York<span class="social-square"></span></li>
      <li>@lakeshoreRealtyQ<span class="social-square"></span></li>
    </ul>
    <div class="contact-band office-band">
      <div class="office">0000, Anywhere, Nowhere<br>City, ST 0000</div>
      <div class="office">222, Anywhere, Nowhere<br>City, ST 2222</div>
      <div class="office">333, Anywhere, Nowhere<br>City, ST 3333</div>
    </div>
  </section>

</body>
</html>
```